Communications & Broadcast Consulting/PR/Media Relations & Public Affairs

My main goals are to provide communications support to school districts, small towns/cities/hospitals and private businesses in the form of press releases, media relations, public affairs. I also have 25 years experience as a television news anchor/reporter and I'm open to free-lance reporting in both Indianapolis and other markets. My specialty is working with the media.
Communications

```html
<!DOCTYPE html>
<html lang="en">
<head>
<meta charset="utf-8">
<title>Brightmast Communications – Business Card</title>
<link href="https://fonts.googleapis.com/css2?family=Arimo:wght@400;700&display=swap" rel="stylesheet">
<style>
  :root {
    --backdrop: #5b4f47;
    --tone-dark: #2a0b08;
    --tone-maroon: #6e1416;
    --tone-red: #b52a1c;
    --tone-orange: #e8641c;
    --tone-gold: #f5a623;
    --accent-yellow: #ffd21f;
    --brand-yellow: #ffd84a;
    --text-light: #ffffff;
  }
  html, body {
    margin: 0;
    padding: 0;
    width: 1200px;
    height: 1200px;
    overflow: hidden;
    background: var(--backdrop);
  }
  .canvas {
    position: relative;
    width: 1200px;
    height: 1200px;
  }
  .business-card {
    position: absolute;
    left: 42px;
    top: 254px;
    width: 1118px;
    height: 654px;
    overflow: hidden;
    font-family: "Arimo", Arial, sans-serif;
    color: var(--text-light);
    box-shadow: 0 6px 18px rgba(0,0,0,0.35);
  }
  .card-artwork {
    position: absolute;
    inset: 0;
    background:
      linear-gradient(90deg, rgba(30,10,5,0.88) 0%, rgba(40,14,6,0.6) 35%, rgba(40,14,6,0) 58%),
      radial-gradient(ellipse 70% 90% at 72% 70%, var(--tone-gold) 0%, var(--tone-orange) 35%, var(--tone-red) 65%, var(--tone-maroon) 85%, var(--tone-dark) 100%);
  }
  .brand {
    position: absolute;
    left: 46px;
    top: 50px;
    display: flex;
    align-items: center;
    gap: 20px;
  }
  .brand-mark {
    width: 92px;
    height: 92px;
    border: 5px solid var(--brand-yellow);
    border-radius: 50%;
    box-sizing: border-box;
    flex: none;
  }
  .brand-name {
    margin: 0;
    font-weight: 700;
    color: var(--brand-yellow);
    font-size: 68px;
    line-height: 1;
    letter-spacing: 1px;
  }
  .brand-name span {
    display: block;
    font-size: 44px;
    margin-top: 4px;
  }
  .contact {
    position: absolute;
    left: 48px;
    top: 260px;
  }
  .person-name {
    margin: 0;
    font-weight: 400;
    font-size: 38px;
    color: var(--accent-yellow);
    line-height: 1.1;
  }
  .person-title {
    margin: 4px 0 0;
    font-size: 26px;
    line-height: 1.2;
  }
  .address {
    margin: 26px 0 0 3px;
    font-style: normal;
    font-size: 26px;
    line-height: 1.48;
  }
  .details {
    list-style: none;
    margin: 12px 0 0 3px;
    padding: 0;
    font-size: 26px;
    line-height: 1.66;
  }
</style>
</head>
<body>
<main class="canvas">
  <article class="business-card">
    <div class="card-artwork" role="img" aria-label="Sunset sky in deep red, orange and gold with a red and white broadcast tower sending out signal rings above a dark grassy horizon"></div>

    <header class="brand">
      <div class="brand-mark"></div>
      <h1 class="brand-name">BRIGHTMAST<span>COMMUNICATIONS</span></h1>
    </header>

    <section class="contact">
      <h2 class="person-name">Dale Brennan</h2>
      <p class="person-title">Public &amp; Media Relations Consultant</p>
      <address class="address">
        Brightmast Communications,<br>
        1827 Alder Row Lane, Fairmont,<br>
        IN 46120
      </address>
      <ul class="details">
        <li>Office : 555.014.2288</li>
        <li>Mobile : 555.018.4471</li>
        <li>Email : dbrennan77@mailbox.com</li>
      </ul>
    </section>
  </article>
</main>
</body>
</html>
```